Very personalised Wedding Invitation

I want a wedding invitation very unique and personalised with the menus, ceremony time table and thank you cards. I want a mix of a nice traditional style with indian style touch. I don't want a colourful invitation, it can have max. two different colours.

The bride's name is Rosalind and the groom's name is Tarun

Reason: None of the designs submitted are what I am looking for

Target Market(s)

Invitations, personalised invitations,

Industry/Entity Type

Wedding

Logo Text

Our initials T&R To use in our wedding things

Font styles to use
Decorative
Script

Requirements
Must have
Nice to have
• I would like a chic design with a bit of indian style
Should not have

```html
<!DOCTYPE html>
<html lang="en">
<head>
<meta charset="utf-8">
<title>Rosalind &amp; Tarun — Wedding Stationery</title>
<link rel="stylesheet" href="https://fonts.googleapis.com/css2?family=Great+Vibes&family=Poiret+One&display=swap">
<style>
  :root {
    --ink: #14161d;
    --gold: #c9a23a;
    --gold-light: #efd77a;
    --gold-deep: #a9811f;
    --paper: #ffffff;
    --backdrop: #ece7df;
    --text-dark: #1d1d22;
  }
  html, body {
    margin: 0;
    padding: 0;
    overflow: hidden;
  }
  body {
    width: 940px;
    height: 1200px;
    background: var(--backdrop);
    position: relative;
    font-family: "Poiret One", sans-serif;
  }

  /* Envelope */
  .envelope {
    position: absolute;
    left: 259px;
    top: 64px;
    width: 413px;
    height: 527px;
  }
  .envelope svg { position: absolute; inset: 0; }
  .envelope-names {
    position: absolute;
    left: 0;
    right: 0;
    top: 440px;
    text-align: center;
    font-family: "Great Vibes", cursive;
    font-size: 46px;
    color: var(--gold);
    line-height: 1;
  }

  /* Cards */
  .card {
    position: absolute;
    top: 620px;
    width: 318px;
    height: 514px;
    background: var(--paper);
    overflow: hidden;
    box-shadow: 0 2px 6px rgba(0,0,0,0.08);
  }
  .card--cover { left: 111px; }
  .card--invite { left: 504px; width: 336px; }

  .medallion {
    position: absolute;
    border-radius: 50%;
    background: radial-gradient(circle, var(--gold-light) 0%, var(--gold) 55%, rgba(201,162,58,0.55) 72%, rgba(201,162,58,0) 73%);
    opacity: 0.85;
  }
  .card--cover .medallion {
    width: 400px;
    height: 400px;
    left: -41px;
    top: 100px;
  }
  .card--invite .medallion {
    width: 220px;
    height: 220px;
    left: 58px;
    top: 448px;
  }

  .name-band {
    position: absolute;
    left: 0;
    right: 0;
    background: var(--ink);
    color: var(--gold);
    font-family: "Great Vibes", cursive;
    text-align: center;
  }
  .card--cover .name-band {
    top: 242px;
    height: 114px;
    font-size: 42px;
    line-height: 114px;
  }
  .card--invite .name-band {
    top: 235px;
    height: 121px;
    font-size: 40px;
    line-height: 1;
    padding-top: 18px;
    box-sizing: border-box;
  }
  .name-band .surnames {
    display: flex;
    justify-content: center;
    gap: 42px;
    margin-top: 2px;
  }
  .name-band svg {
    position: absolute;
    left: 0;
    width: 100%;
    pointer-events: none;
  }

  .invite-text {
    position: absolute;
    left: 0;
    right: 0;
    text-align: center;
    color: var(--text-dark);
    text-transform: uppercase;
    font-size: 14px;
    letter-spacing: 0.4px;
    line-height: 1.25;
  }
  .invite-text--top { top: 70px; }
  .invite-text--bottom {
    top: 374px;
    font-size: 13px;
    line-height: 1.15;
  }
  .invite-text .hosts {
    font-family: "Great Vibes", cursive;
    text-transform: none;
    font-size: 27px;
    letter-spacing: 0;
    line-height: 1.15;
    margin: 2px 0;
  }
  .invite-text p { margin: 0; }
</style>
</head>
<body>

  <section class="envelope" aria-label="Envelope">
    <svg width="413" height="527" viewBox="0 0 413 527">
      <defs>
        <radialGradient id="linerTone" cx="50%" cy="45%" r="60%">
          <stop offset="0" stop-color="#e3c15a"/>
          <stop offset="0.6" stop-color="#f3e4b0"/>
          <stop offset="1" stop-color="#fbf6e6"/>
        </radialGradient>
      </defs>
      <polygon points="0,170 206,0 413,170 413,527 0,527" fill="var(--ink)"/>
      <polygon points="26,176 206,28 387,176 387,390 26,390" fill="url(#linerTone)"
               role="img" aria-label="Gold mandala pattern on envelope liner"/>
      <path d="M0,375 Q206,395 413,375 L413,527 L0,527 Z" fill="var(--ink)"/>
      <path d="M30,488 Q120,500 210,486 T400,470" fill="none" stroke="var(--gold)" stroke-width="1.4"/>
    </svg>
    <div class="envelope-names">Rosalind &amp; Tarun</div>
  </section>

  <article class="card card--cover" aria-label="Invitation cover">
    <div class="medallion" role="img" aria-label="Gold mandala medallion"></div>
    <div class="name-band">
      Rosalind &amp; Tarun
      <svg height="114" viewBox="0 0 318 114" preserveAspectRatio="none" style="top:0">
        <path d="M8,80 Q90,88 170,78 T312,70" fill="none" stroke="var(--gold)" stroke-width="1.2"/>
      </svg>
    </div>
  </article>

  <article class="card card--invite" aria-label="Invitation">
    <div class="invite-text invite-text--top">
      <p>With our hearts full of joy</p>
      <p class="hosts">Mr and Mrs Ashcombe</p>
      <p>Together with</p>
      <p class="hosts">Mr and Mrs Mehra</p>
      <p>Request the honor of your presence at<br>the mariage of their beloved children</p>
    </div>

    <div class="name-band">
      <div>Rosalind &amp; Tarun</div>
      <div class="surnames"><span>Ashcombe</span><span>Mehra</span></div>
      <svg height="121" viewBox="0 0 336 121" preserveAspectRatio="none" style="top:0">
        <path d="M6,62 Q80,70 168,58 T330,50" fill="none" stroke="var(--gold)" stroke-width="1.2"/>
      </svg>
    </div>

    <div class="invite-text invite-text--bottom">
      <p>On September, the 23rd,2016 at six o'clock</p>
      <p>in the evening,</p>
      <p>Random Event Saloon name</p>
      <p>located in random adress</p>
    </div>

    <div class="medallion" role="img" aria-label="Gold mandala medallion"></div>
  </article>

</body>
</html>
```